Wordpress theme website for professionals working together

My partner and I are offering business services, my wife in the energy business as mainly as member of the board of commissioners. I am working as interim manager/consultant in the accounting and finance area. Both activities are connected in one company VELMORO BV (dutch ltd). We need a CV based website. Beside this we do some financial and accounting services.

Target Market(s)

small medium business

Font styles to use
Sans Serif

Colors

Designer to choose colors to be used in the design.

Requirements
Must have
• Pictures of both members.
• CLEAN AND SIMPLE
• I LIKE BLACK & WHITE
Nice to have
• I like design like this theme: http://theme.brindlepax.com/resume/

```html
<!DOCTYPE html>
<html lang="en">
<head>
<meta charset="utf-8">
<title>Marten – Resume</title>
<link rel="stylesheet" href="https://fonts.googleapis.com/css2?family=Noto+Sans:wght@300;400&display=swap">
<style>
  :root {
    --ink: #111111;
    --paper: #ffffff;
    --muted: #a0a0a0;
    --panel: #121212;
    --photo-tone: #8a8580;
    --shadow: rgba(0,0,0,0.22);
  }
  * { box-sizing: border-box; margin: 0; padding: 0; }
  html, body { width: 1200px; height: 800px; overflow: hidden; background: var(--paper); }
  body { font-family: "Noto Sans", sans-serif; color: var(--ink); position: relative; }

  .resume {
    position: absolute; left: 50px; top: 50px; width: 1100px; height: 700px;
    background: var(--paper); box-shadow: 10px 12px 14px var(--shadow);
  }

  /* Profile panel */
  .profile {
    position: absolute; left: 0; top: 0; width: 400px; height: 700px;
    background: var(--panel); color: var(--paper); text-align: center;
  }
  .portrait-ring {
    position: absolute; left: 75px; top: 87px; width: 250px; height: 250px;
    border-radius: 50%; border: 3px solid var(--paper); padding: 6px;
  }
  .portrait {
    width: 100%; height: 100%; border-radius: 50%;
    background: radial-gradient(circle at 50% 40%, #cfc6bf 0%, #a79c94 45%, var(--photo-tone) 75%, #4a4f63 100%);
  }
  .profile-rule { position: absolute; left: 83px; top: 349px; width: 235px; height: 1px; background: var(--paper); }
  .profile-name { position: absolute; left: 0; top: 350px; width: 100%; font-size: 56px; font-weight: 300; letter-spacing: 1px; line-height: 70px; }
  .profile-role { position: absolute; left: 0; width: 100%; font-size: 15px; font-weight: 400; line-height: 20px; }
  .profile-role.first { top: 413px; }
  .profile-role.second { top: 435px; }
  .profile-pager { position: absolute; left: 177px; top: 649px; display: flex; gap: 16px; }
  .pager-dot { width: 14px; height: 14px; border-radius: 50%; background: var(--muted); }
  .pager-dot.active { background: var(--paper); }
  .pager-dot.dark { background: var(--ink); }

  /* Content */
  .section-head {
    position: absolute; left: 433px; width: 630px; height: 26px;
    display: flex; align-items: center; font-size: 22px; font-weight: 400; line-height: 26px;
  }
  .section-head::after {
    content: ""; flex: 1; height: 2px; background: var(--ink); margin-left: 2px;
  }
  .section-head .bar {
    position: absolute; right: 0; top: 9px; width: 116px; height: 8px; display: block;
  }
  .item {
    position: absolute; left: 455px; font-size: 19px; font-weight: 400; line-height: 24px; white-space: nowrap;
  }
  .item::before { content: "•"; margin-right: 4px; }
  .item-note { position: absolute; left: 468px; font-size: 10.5px; line-height: 14px; white-space: nowrap; }

  .skill { position: absolute; left: 543px; width: 420px; height: 24px; display: flex; align-items: center; }
  .skill-name { font-size: 19px; line-height: 24px; width: 280px; }
  .skill-level { display: flex; gap: 15px; }
  .skill-level i { width: 14px; height: 14px; border-radius: 50%; background: var(--ink); display: block; }
  .skill-level i.off { background: var(--muted); }

  .content-pager { position: absolute; left: 713px; top: 649px; display: flex; gap: 15px; }
</style>
</head>
<body>
<main class="resume">
  <aside class="profile">
    <div class="portrait-ring"><div class="portrait" role="img" aria-label="Portrait photo of Marten"></div></div>
    <div class="profile-rule"></div>
    <h1 class="profile-name">MARTEN</h1>
    <p class="profile-role first">Advisor RDK</p>
    <p class="profile-role second">Advisor Halden &amp; Keller</p>
    <div class="profile-pager"><span class="pager-dot"></span><span class="pager-dot active"></span></div>
  </aside>

  <h2 class="section-head" style="top:20px">FINISHED JOBS<svg class="bar" viewBox="0 0 116 8"><polygon points="6,0 116,0 116,8 0,8" fill="#111"/></svg></h2>
  <p class="item" style="top:48px">Controller a.i. RDK</p>
  <p class="item-note" style="top:73px">Led monthly closing, budgets and reporting for the finance team during a period of change</p>
  <p class="item" style="top:91px">Advisor Solvane Green</p>
  <p class="item-note" style="top:116px">Advised the board on cash flow, funding and risk while preparing the company for new growth</p>
  <p class="item" style="top:134px">Financial director Norvest</p>
  <p class="item-note" style="top:159px">Directed finance, control and annual accounts and built a lean team for the full group</p>

  <h2 class="section-head" style="top:177px">EDUCATION<svg class="bar" viewBox="0 0 116 8"><polygon points="6,0 116,0 116,8 0,8" fill="#111"/></svg></h2>
  <p class="item" style="top:205px">Auditra (RA)</p>
  <p class="item" style="top:230px">Atheneum B</p>

  <h2 class="section-head" style="top:259px">WORKED FOR<svg class="bar" viewBox="0 0 116 8"><polygon points="6,0 116,0 116,8 0,8" fill="#111"/></svg></h2>
  <p class="item" style="top:289px">Holtrop Advocaten &amp; Notarissen</p>
  <p class="item" style="top:314px">Kestrel Audit</p>

  <h2 class="section-head" style="top:341px">SKILL&nbsp;<svg class="bar" viewBox="0 0 116 8"><polygon points="6,0 116,0 116,8 0,8" fill="#111"/></svg></h2>
  <div class="skill" style="top:376px"><span class="skill-name">Accounting</span><span class="skill-level"><i></i><i></i><i></i><i></i><i></i></span></div>
  <div class="skill" style="top:405px"><span class="skill-name">Annual reporting</span><span class="skill-level"><i></i><i></i><i></i><i></i><i class="off"></i></span></div>
  <div class="skill" style="top:434px"><span class="skill-name">Financial management</span><span class="skill-level"><i></i><i></i><i></i><i class="off"></i><i class="off"></i></span></div>
  <div class="skill" style="top:464px"><span class="skill-name">Financial monthly reporting</span><span class="skill-level"><i></i><i></i><i></i><i class="off"></i><i class="off"></i></span></div>
  <div class="skill" style="top:493px"><span class="skill-name">Project management</span><span class="skill-level"><i></i><i></i><i></i><i class="off"></i><i class="off"></i></span></div>
  <div class="skill" style="top:522px"><span class="skill-name">Team player</span><span class="skill-level"><i></i><i></i><i></i><i></i><i class="off"></i></span></div>
  <div class="skill" style="top:553px"><span class="skill-name">Trouble shooter</span><span class="skill-level"><i></i><i></i><i></i><i></i><i class="off"></i></span></div>

  <h2 class="section-head" style="top:585px">OTHER<svg class="bar" viewBox="0 0 116 8"><polygon points="6,0 116,0 116,8 0,8" fill="#111"/></svg></h2>
  <p class="item" style="top:614px">Photography</p>

  <div class="content-pager"><span class="pager-dot dark"></span><span class="pager-dot"></span><span class="pager-dot"></span></div>
</main>
</body>
</html>
```